Postcard Design

We need a postcard design for our company, Calvera Business Group. Our firm sources funding (money) solutions for existing small business owners and start-up who are seeking $50,000 to $250,000. We would like to see designs that feature the colors dark or navy blue and gold. (We are uploading our logo for color reference ONLY. We DO NOT want the logo to be a part of the design!) The final design should communicate that we are an established financial source for business owners who are looking for capital to borrow. The final design should also emphasize that we provide quick approval and fast turnaround.
Target Market(s)
Small business owners (less than 10 employees) as well as start-up companies.
Industry/Entity Type
Small Business

```html
<!DOCTYPE html>
<html lang="en">
<head>
<meta charset="utf-8">
<title>Calvera Business Group – Postcard</title>
<link rel="stylesheet" href="https://fonts.googleapis.com/css2?family=Cinzel:wght@500;600&family=Cormorant+Garamond:wght@500;600&display=swap">
<style>
  :root {
    --gold: #f2c22e;
    --gold-deep: #e0a816;
    --navy: #27388f;
    --navy-deep: #1c2a6e;
    --navy-light: #3449b0;
    --charcoal: #333333;
    --stage: #3a3a3a;
    --white: #ffffff;
    --ink: #1b1b1b;
    --photo-a: #cfd6dc;
    --photo-b: #6f7885;
  }
  * { margin: 0; padding: 0; box-sizing: border-box; }
  html, body { width: 789px; height: 1200px; overflow: hidden; }
  body {
    background: var(--stage); position: relative;
    font-family: "Cormorant Garamond", Georgia, serif;
    font-variant-numeric: lining-nums;
  }
  .card { position: absolute; left: 62px; overflow: hidden; }
  .block { position: absolute; }

  /* Front */
  .front { top: 62px; width: 667px; height: 517px; background: var(--white); }
  .front .photo {
    left: 0; top: 28px; width: 667px; height: 372px;
    background: linear-gradient(120deg, var(--photo-a) 0%, #e9ecef 35%, var(--photo-b) 60%, #c9ced4 100%);
  }
  .front .top-strip { left: 0; top: 0; width: 667px; height: 28px; background: linear-gradient(90deg, var(--gold), var(--gold-deep)); }
  .front .name-box { left: 0; top: 0; width: 258px; height: 135px; background: linear-gradient(90deg, var(--gold), var(--gold-deep)); }
  .brand-name {
    position: absolute; left: 0; top: 20px; width: 258px; text-align: center;
    font-family: "Cinzel", "Times New Roman", serif; font-weight: 500;
    font-size: 35px; line-height: 38px; color: var(--navy-deep);
  }
  .front .banner-step { left: 443px; top: 338px; width: 224px; height: 62px; background: var(--navy); }
  .front .banner { left: 188px; top: 395px; width: 479px; height: 122px; background: linear-gradient(90deg, var(--navy-light), var(--navy-deep)); }
  .front .corner-gold { left: 0; top: 395px; width: 186px; height: 122px; background: linear-gradient(90deg, var(--gold-deep), var(--gold)); }
  .front .corner-navy { left: 0; top: 435px; width: 128px; height: 82px; background: var(--navy); }
  .front .corner-navy-inner { left: 63px; top: 473px; width: 65px; height: 44px; background: var(--navy-deep); }
  .headline, .subline {
    position: absolute; left: 214px; width: 430px;
    font-family: "Cinzel", "Times New Roman", serif; font-weight: 500;
    text-transform: uppercase; white-space: nowrap;
  }
  .headline { top: 411px; color: var(--gold); font-size: 34px; line-height: 40px; letter-spacing: 1px; }
  .subline { top: 451px; color: var(--white); font-size: 27px; line-height: 36px; letter-spacing: 2px; }

  /* Back */
  .back { top: 623px; width: 669px; height: 519px; background: var(--white); }
  .back .panel { left: 0; top: 0; width: 350px; height: 519px; background: var(--charcoal); }
  .back .corner-gold { left: 0; top: 0; width: 155px; height: 122px; background: linear-gradient(180deg, var(--gold), var(--gold-deep)); }
  .back .corner-navy { left: 0; top: 0; width: 103px; height: 85px; background: linear-gradient(135deg, var(--navy-light), var(--navy-deep)); }
  .back .corner-navy-inner { left: 43px; top: 0; width: 60px; height: 47px; background: var(--navy); }
  .back .emblem { left: 160px; top: 130px; width: 120px; height: 230px; background: #383838; border-radius: 12px; }
  .about-title {
    position: absolute; left: 172px; top: 68px;
    font-family: "Cinzel", "Times New Roman", serif; color: var(--gold); font-weight: 600;
    font-size: 33px; line-height: 42px; white-space: nowrap;
  }
  .about-rule { left: 243px; top: 115px; width: 97px; height: 6px; background: var(--gold); }
  .about-copy {
    position: absolute; left: 28px; top: 157px; width: 316px;
    color: var(--white); font-size: 18.5px; line-height: 25px; font-weight: 500;
    white-space: nowrap;
  }
  .about-copy p { margin-bottom: 12px; }
  .back .contact-tab { left: 0; top: 430px; width: 192px; height: 50px; background: var(--gold); }
  .back .contact-band { left: 0; top: 475px; width: 350px; height: 44px; background: linear-gradient(90deg, var(--gold), var(--gold-deep)); }
  .contact { position: absolute; left: 16px; top: 443px; color: var(--navy-deep); font-size: 24px; line-height: 26px; font-weight: 600; white-space: nowrap; }
  .contact div { display: flex; align-items: center; gap: 8px; }
  .contact svg { width: 14px; height: 14px; flex: none; }
  .stamp { left: 586px; top: 107px; width: 53px; height: 61px; border: 1.5px solid var(--ink); }
  .address-line { left: 437px; width: 216px; height: 1.5px; background: var(--ink); }
</style>
</head>
<body>
  <section class="card front" aria-label="Postcard front">
    <div class="block photo" role="img" aria-label="Photo of business people meeting and shaking hands at a table with a laptop"></div>
    <div class="block top-strip"></div>
    <div class="block name-box"><h1 class="brand-name">Calvera<br>Business<br>Group</h1></div>
    <div class="block banner-step"></div>
    <div class="block banner"></div>
    <div class="block corner-gold"></div>
    <div class="block corner-navy"></div>
    <div class="block corner-navy-inner"></div>
    <p class="headline">Financial Source</p>
    <p class="subline">For Business Owners</p>
  </section>

  <section class="card back" aria-label="Postcard back">
    <div class="block panel"></div>
    <div class="block emblem" role="img" aria-label="Faint money bag illustration"></div>
    <div class="block corner-gold"></div>
    <div class="block corner-navy"></div>
    <div class="block corner-navy-inner"></div>
    <h2 class="about-title">About Us</h2>
    <div class="block about-rule"></div>
    <div class="about-copy">
      <p>Our firm sources funding (money)<br>solutions for existing small business owners<br>and start-up who are seeking $50,000 to<br>$250,000.</p>
      <p>We are an established financial source for<br>business owners who are looking for capital<br>to borrow.</p>
      <p>We also provide quick approval and fast<br>turnaround.</p>
    </div>
    <div class="block contact-tab"></div>
    <div class="block contact-band"></div>
    <div class="contact">
      <div><svg viewBox="0 0 14 14" aria-hidden="true"><rect x="2" y="1" width="10" height="12" rx="1.5" fill="var(--navy-deep)"/><rect x="4" y="3" width="6" height="3" fill="var(--gold)"/><rect x="4" y="8" width="2" height="1.5" fill="var(--gold)"/><rect x="8" y="8" width="2" height="1.5" fill="var(--gold)"/><rect x="4" y="10.5" width="2" height="1.5" fill="var(--gold)"/><rect x="8" y="10.5" width="2" height="1.5" fill="var(--gold)"/></svg>555-214-0387</div>
      <div><svg viewBox="0 0 14 14" aria-hidden="true"><circle cx="7" cy="7" r="6" fill="var(--navy-deep)"/><path d="M1 7h12M7 1c-3 3-3 9 0 12M7 1c3 3 3 9 0 12" stroke="var(--gold)" stroke-width="0.9" fill="none"/></svg>www.calvera.example</div>
    </div>
    <div class="block stamp"></div>
    <div class="block address-line" style="top:283px"></div>
    <div class="block address-line" style="top:315px"></div>
    <div class="block address-line" style="top:347px"></div>
  </section>
</body>
</html>
```